Delta Ridge Arms

Firearms Website

Requirements
Must have
• we are looking for two or three pages for a new company we are starting. The Name is Delta Ridge Arms. The site will be DeltaRidgeArms.example (nothing on site at this time) We will be selling mainly handguns and products for self defense. We want this site to focus on the handgun and ammo sells as well as low cost transfers. we will handle the ecommerce part) We want a

1.) main page, mainly general information on the company.

2.) a page for sells. we will be adding the guns by hand as we place them for sell and use our credit card process. We just need the layout to fill in the items for sale on this page.

3.) navigation will be.. HOME - SALES (((guns and gun Accessories)) and self defense products) - Contact US- Transfers

company info

Delta Ridge Arms

DeltaRidgeArms.example

sales@DeltaRidgeArms.example

855-Bolt 2 Save (855-265-2728) same number for fax

412 south Walnut street

Pinebrook, ms. 39000

```html
<!DOCTYPE html>
<html lang="en">
<head>
<meta charset="utf-8">
<title>Delta Ridge Arms</title>
<link href="https://fonts.googleapis.com/css2?family=PT+Sans+Narrow:wght@400;700&family=Arimo:wght@400;700&display=swap" rel="stylesheet">
<style>
:root{
  --orange:#f04a14;
  --orange-dark:#c9360a;
  --ink:#111;
  --nav:#5a5a5a;
  --panel:#5b5b5b;
  --footer:#1c1c1c;
  --text-light:#fff;
  --text-muted:#b8b8b8;
  --line:#777;
}
*{box-sizing:border-box;margin:0;padding:0}
html,body{width:1186px;height:1200px;overflow:hidden;background:#111}
.page{width:1000px;height:1012px;position:relative;transform:scale(1.186);transform-origin:0 0;font-family:"Arimo",Arial,sans-serif;color:var(--text-light)}
.condensed{font-family:"PT Sans Narrow","Arial Narrow",sans-serif;font-weight:700}

.site-header{position:absolute;left:0;top:0;width:1000px;height:130px;background:linear-gradient(90deg,#1a1a1a 0%,#2e2e2e 45%,#3c3c3c 70%,#262626 100%);border-bottom:1px solid var(--line)}
.brand{position:absolute;left:22px;top:32px;display:flex;align-items:center;gap:10px;font-size:40px;color:var(--orange);letter-spacing:1px;line-height:1}
.brand-mark{width:16px;height:16px;background:var(--orange)}
.search{position:absolute;left:820px;top:20px;width:160px;height:20px;background:#000;border:1px solid #444;border-radius:5px;font-size:11px;color:#ddd;padding:3px 8px}
.search svg,.newsletter svg,.btn svg{position:absolute}
.search svg{right:6px;top:3px}
.main-nav{position:absolute;left:359px;top:65px;width:622px;height:38px;background:linear-gradient(#6a6a6a,#4e4e4e);border:1px solid #888;border-radius:5px}
.main-nav a{position:absolute;top:6px;font-size:17px;color:#fff;text-decoration:none;line-height:24px}
.main-nav .active{left:7px;padding:0 13px;background:#fff;color:var(--orange);border-radius:4px}
.currency{position:absolute;left:447px;top:10px;font-family:"Arimo",Arial,sans-serif;font-weight:400;font-size:12px;color:#fff}
.currency-select{position:absolute;left:509px;top:6px;width:104px;height:22px;background:linear-gradient(#6d6d6d,#555);border:1px solid #999;border-radius:4px;font-family:"Arimo",Arial,sans-serif;font-weight:400;font-size:11px;color:#ccc;padding:4px 10px}
.currency-select svg{position:absolute;right:8px;top:7px}

.hero{position:absolute;left:25px;top:133px;width:956px;height:322px;background:linear-gradient(135deg,#1d1d1d,#0d0d0d 60%,#1a1a1a)}
.hero-photo{position:absolute;left:0;top:0;width:480px;height:322px;background:radial-gradient(ellipse at 45% 45%,#3a3a3a,#151515 70%)}
.hero-title{position:absolute;left:489px;top:32px;width:470px;font-size:30px;line-height:38px;color:var(--orange)}
.hero-text{position:absolute;left:489px;top:124px;width:470px;font-size:22px;line-height:30px;color:#fff}
.btn{position:absolute;width:158px;height:33px;border-radius:17px;background:linear-gradient(#f4f4f4,#bdbdbd);border:1px solid #999;color:var(--orange);font-size:20px;padding:3px 0 0 14px}
.btn svg{right:12px;top:9px}
.hero .btn{left:487px;top:213px}
.dots{position:absolute;left:846px;top:295px;display:flex;gap:8px}
.dots span{width:12px;height:12px;border-radius:50%;border:1.5px solid #ccc}
.dots .on{background:var(--orange);border-color:var(--orange)}

.welcome{position:absolute;left:0;top:457px;width:1000px;height:376px;background:linear-gradient(90deg,#4e4e4e,#646464 50%,#565656);border-top:1px solid #888}
.welcome h1{position:absolute;left:24px;top:32px;font-size:36px;font-weight:700;line-height:40px}
.welcome h1 em{font-style:normal;color:var(--orange)}
.intro{position:absolute;left:24px;top:86px;width:627px;font-size:12px;line-height:20px;text-align:justify}
.intro p+p{margin-top:20px}
.welcome .btn{left:24px;top:289px}
.promo{position:absolute;left:673px;width:308px;height:153px;border:1px solid #aaa;border-radius:4px;overflow:hidden}
.promo-a{top:32px;background:linear-gradient(135deg,#2a2a2a,#555 60%,#3a3a3a)}
.promo-b{top:203px;background:linear-gradient(135deg,#6b4a2d,#a06a3a 50%,#5a4030)}
.promo-label{position:absolute;right:6px;top:52px;text-align:right;font-family:"PT Sans Narrow",sans-serif;font-weight:700;font-style:italic;color:#fff;font-size:30px;line-height:26px}
.promo-label small{display:block;font-size:20px}
.buy{position:absolute;left:0;bottom:0;width:100%;height:35px;background:linear-gradient(90deg,var(--orange-dark),var(--orange) 40%,rgba(240,74,20,.2));color:#fff;font-size:21px;padding:3px 12px}

.site-footer{position:absolute;left:0;top:833px;width:1000px;height:179px;background:linear-gradient(#2a2a2a,var(--footer) 20%,#161616);border-top:1px solid #3a3a3a}
.col{position:absolute;top:35px}
.col h2{font-size:17px;line-height:20px;color:#fff;font-weight:700}
.col p,.col li{font-size:12px;line-height:14px;color:var(--text-muted);list-style:none}
.col-home{left:22px;width:130px}
.col-home p{margin-top:19px}
.col-sales{left:188px;width:130px}
.col-sales ul{margin-top:20px}
.col-sales li{margin-bottom:14px}
.col-contact{left:353px;width:260px}
.col-contact ul{margin-top:19px}
.col-contact li{margin-bottom:10px}
.col-contact b{color:#fff}
.col-news{left:763px;width:220px}
.col-news h2{color:#ccc}
.newsletter{position:relative;margin-top:21px;width:217px;height:31px;border-radius:5px;background:linear-gradient(#f2f2f2,#c8c8c8);color:#555;font-size:14px;padding:7px 13px}
.newsletter svg{right:8px;top:9px}
.copy{position:absolute;right:19px;top:134px;font-size:11px;color:#bbb}
</style>
</head>
<body>
<div class="page">
  <header class="site-header" role="img" aria-label="Header photo of a shooter aiming a rifle on a dark background">
    <div class="brand condensed"><span class="brand-mark"></span>DELTA RIDGE ARMS</div>
    <div class="search">Write your text here
      <svg width="14" height="14" viewBox="0 0 14 14"><circle cx="7" cy="7" r="6" fill="none" stroke="#f04a14" stroke-width="1.5"/><path d="M4 7h5M7 4.5 9.5 7 7 9.5" fill="none" stroke="#f04a14" stroke-width="1.5"/></svg>
    </div>
    <nav class="main-nav condensed">
      <a class="active" href="#">HOME</a>
      <a href="#" style="left:85px">SALES</a>
      <a href="#" style="left:150px">CONTACT US</a>
      <a href="#" style="left:251px">TRANSFERS</a>
      <span class="currency">Currency</span>
      <div class="currency-select">Dollar
        <svg width="10" height="6" viewBox="0 0 10 6"><path d="M0 0h10L5 6z" fill="#fff"/></svg>
      </div>
    </nav>
  </header>

  <section class="hero">
    <div class="hero-photo" role="img" aria-label="Black semi-automatic handgun with a row of brass cartridges"></div>
    <h2 class="hero-title condensed">Lorem ipsum dolor sit amet, consectetur adipiscing elit fusce sollicitudin lobortis</h2>
    <p class="hero-text condensed">In congue vulputate tincidunt. Vivamus pretium nulla a lectus ullamcorper eleifend. Sed non egestas tellus.</p>
    <a class="btn condensed">More Details
      <svg width="14" height="14" viewBox="0 0 14 14"><circle cx="7" cy="7" r="6" fill="none" stroke="#f04a14" stroke-width="1.5"/><path d="M4 7h5M7 4.5 9.5 7 7 9.5" fill="none" stroke="#f04a14" stroke-width="1.5"/></svg>
    </a>
    <div class="dots"><span class="on"></span><span></span><span></span><span></span><span></span></div>
  </section>

  <section class="welcome">
    <h1 class="condensed"><em>Welcome to</em> Delta Ridge Arms</h1>
    <div class="intro">
      <p>Cras felis nisl, venenatis at sodales nec, sagittis ac mauris. Vestibulum in magna in sem bibendum pretium at vel urna. Suspendisse vestibulum tempor volutpat. Cras at neque ut lacus feugiat tempor. Nulla hendrerit leo vitae ligula pharetra mattis. Nunc placerat pharetra risus, ut suscipit risus rutrum nec. Duis nunc purus, congue quis mollis vitae, accumsan in quam. Quisque tempor consectetur purus, ut hendrerit neque congue quis. Vestibulum massa massa, dictum non volutpat ut, vehicula a odio.<br>Phasellus mattis sodales eros, vitae luctus purus hendrerit a. Proin tempus arcu nec arcu commodo adipiscing.</p>
      <p>Integer consequat neque sit amet tellus bibendum dictum. Morbi at ante ante, et condimentum lectus. Sed velit quam, rutrum ut feugiat vitae, congue ac eros. Sed non neque viverra diam suscipit fringilla in ac metus.</p>
    </div>
    <a class="btn condensed">More Details
      <svg width="14" height="14" viewBox="0 0 14 14"><circle cx="7" cy="7" r="6" fill="none" stroke="#f04a14" stroke-width="1.5"/><path d="M4 7h5M7 4.5 9.5 7 7 9.5" fill="none" stroke="#f04a14" stroke-width="1.5"/></svg>
    </a>
    <div class="promo promo-a" role="img" aria-label="Close-up of a custom pistol on a dark cloth">
      <div class="promo-label">IRONHOLLOW<small>V2 45ACP CUSTOM</small></div>
      <div class="buy condensed">Buy Now &gt;</div>
    </div>
    <div class="promo promo-b" role="img" aria-label="Leather holster and accessories on a wooden surface">
      <div class="buy condensed">Buy Now &gt;</div>
    </div>
  </section>

  <footer class="site-footer">
    <div class="col col-home">
      <h2 class="condensed">HOME</h2>
      <p>Cras felis nisl, venenatis at sodales nec, sagittis ac mauris. Vestibulum in magna in sem bibendum pretium at vel urna.</p>
    </div>
    <div class="col col-sales">
      <h2 class="condensed">SALES</h2>
      <ul><li>HandGuns</li><li>Guns and Gun Accessories</li><li>Self Defense Products</li></ul>
    </div>
    <div class="col col-contact">
      <h2 class="condensed">CONTACT US</h2>
      <ul>
        <li><b>Email:</b> sales@DeltaRidgeArms.example</li>
        <li><b>Phone No:</b> 855-265-2728</li>
        <li><b>Address:</b> 412 south Walnut street</li>
        <li>Pinebrook, ms. 39000</li>
      </ul>
    </div>
    <div class="col col-news">
      <h2 class="condensed">For Daily Newsletter</h2>
      <div class="newsletter">Write your email here
        <svg width="14" height="14" viewBox="0 0 14 14"><circle cx="7" cy="7" r="6" fill="none" stroke="#f04a14" stroke-width="1.5"/><path d="M4 7h5M7 4.5 9.5 7 7 9.5" fill="none" stroke="#f04a14" stroke-width="1.5"/></svg>
      </div>
    </div>
    <p class="copy">© Copyright reserved 2013. All right reserved.</p>
  </footer>
</div>
</body>
</html>
```